July 2022 Industrial Manufacturer Product Expo Mexico City

We manufacture large screws and fastners for large Mining equipment, Trains, large ships, airplanes, wind turbines, and so on. We also do custom work base on the customer needs. No matter the size we can make it.
We have a Expo coming up with companies all over the world. We have to stand out we are a family own business so our customer service will be above and beyond anyone can provide. We do not have a sales force to push our products and services we provide one on one service.
Plus@!! I'm looking for anything that you designers can come up with if it was your company to put on a business card, plus i want to do a 1 or 2 sided pamphlet, and then a website. We make Speciality Bolts for large mining equipment these bolts can be 3 to 4 foot long!!! Plus fasteners, Nuts, washers, any, size, strengths, special materials, we offer more of a ono on one customer service, We are a small company, family own, but can fulfill any type of orders. We can also provide special time lines for emergency orders. "We keep the machines running we here at KRV don't believe in down time" We want to hear any slogan based on our company to stand out.
Thanks i really appreciate all your work and options that we have to pick on. Plus just a thought we could possibly want to entertain a experience Marketing internet help maybe a employment possibility. Thanks
Updates

I need 2 cards one in Spanish and English Like the steel back ground maybe send me in some bright red and blue writing Same with the Black cards Please remove the word Military The logo KRV maybe integrate a picture of a Bolt 🔩 Thank you

Still looking for I need 2 cards one in Spanish and English Like the steel back ground maybe send me in some bright red and blue writing Same with the Black cards try bright writing Please remove the word Military The logo KRV maybe integrate a picture of a Bolt 🔩 Plus will need the company to make a brochure and website next Thank you

Target Market(s)

Large Mining, Ship, Train, Green Energy, ORBA, and Government equipment. Throughout the World

Industry/Entity Type

We can Custom Manufacture any type of Fastners for Mining equipment, Trains, Ships, Green energy, Governments, or military projects. wind turbines,

Contact Information for Business Card

I attached the name and contact info that's on a card, plus the Company Logo. Would like industrial looking background with Bright Colors that will stand out!! If we can insert somewhere maybe on back that we "Custom Manufacture Any Size or Quantity Fastners for Large Mining Equipment, Trains, Ships, Green Energy Equipment or Government Projects

Font styles to use
Other font styles liked:
• You Pick, has to be bold, colorful standout, Professional looking Beable to read it.

Colors

Designer to choose colors to be used in the design.

Requirements
Must have
• Need in Spanish and English TO STANDOUT FROM THE REST OF THE EXPO!! See Business card details, Rounded corners
Nice to have
• Can i see some of the darker cards with Bright Red and Blue letters I like to see the different type of card material, heavy thickness, plastic, transparent, Metal types, Bright Colors, I saw like Raised letters like on the logo.

```html
<!DOCTYPE html>
<html lang="en">
<head>
<meta charset="utf-8">
<title>KRV Business Cards – English & Spanish</title>
<link href="https://fonts.googleapis.com/css2?family=PT+Sans:wght@400;700&display=swap" rel="stylesheet">
<style>
  :root{
    --stage:#2b2b2d;
    --card:#bdbdbf;
    --blue:#0b1f7a;
    --logo-blue:#1466c8;
    --red:#e3141a;
    --label-red:#b3161b;
    --rule:#8e8e90;
  }
  *{margin:0;padding:0;box-sizing:border-box}
  html,body{width:1200px;height:576px;overflow:hidden;background:var(--stage)}
  body{position:relative;font-family:"PT Sans",sans-serif}
  .column-label{position:absolute;top:52px;font-size:26px;font-weight:700;color:var(--label-red);width:280px;text-align:center}
  .card{position:absolute;width:278px;height:172px;background:var(--card);border-radius:6px;overflow:hidden;text-align:center}
  .brand{position:absolute;left:0;right:0;top:26px;display:flex;justify-content:center;align-items:center;gap:8px}
  .brand-mark{width:14px;height:14px;background:var(--logo-blue)}
  .brand-name{font-size:40px;font-weight:700;color:var(--logo-blue);letter-spacing:6px;line-height:1}
  .front-info{position:absolute;left:0;right:0;bottom:18px}
  .person{font-size:11px;font-weight:700;color:var(--blue)}
  .person.large{font-size:12.5px}
  .role,.contact{font-size:9px;font-weight:700;color:var(--red);line-height:1.3}
  .rule{width:40px;height:1px;background:var(--rule);margin:5px auto}
  .phone-icon{width:8px;height:8px;vertical-align:-1px;margin-right:3px}
  .bolt-art{position:absolute;left:26px;top:0;width:260px;height:172px;background:radial-gradient(ellipse at 60% 50%,#d0d0d2 0%,#b4b4b6 55%,rgba(189,189,191,0) 75%)}
  .back .brand{top:38px}
  .services{position:absolute;left:0;right:0;bottom:14px;font-weight:700;color:var(--red)}
  .services.en{font-size:7.6px;line-height:1.35}
  .services.es{font-size:9px;line-height:1.25}
</style>
</head>
<body>
  <h2 class="column-label" style="left:93px">English</h2>
  <h2 class="column-label" style="left:450px">Spanish</h2>

  <!-- English front -->
  <section class="card front" style="left:95px;top:109px">
    <div class="brand"><span class="brand-name">KRV</span><span class="brand-mark"></span></div>
    <div class="front-info">
      <p class="person large">Dorian Velasco</p>
      <p class="role">Director of Sales &amp; Marketing</p>
      <div class="rule"></div>
      <p class="contact">dvelasco.krv@mailbox.test</p>
      <p class="contact"><svg class="phone-icon" viewBox="0 0 10 10"><path d="M2 1 L4 1 L4.6 3 L3.4 3.8 Q4.3 5.8 6.2 6.6 L7 5.4 L9 6 L9 8 Q9 9 8 9 Q1 8.5 1 2 Q1 1 2 1Z" fill="var(--blue)"/></svg>011521(555)0194826</p>
    </div>
  </section>

  <!-- Spanish front A -->
  <section class="card front" style="left:453px;top:109px">
    <div class="brand"><span class="brand-name">KRV</span><span class="brand-mark"></span></div>
    <div class="front-info" style="bottom:21px">
      <p class="person">Gerente Gral. Marisol Ortega Ruiz</p>
      <div class="rule" style="margin:7px auto"></div>
      <p class="contact">marisolor.krv@mailbox.test</p>
      <p class="contact"><svg class="phone-icon" viewBox="0 0 10 10"><path d="M2 1 L4 1 L4.6 3 L3.4 3.8 Q4.3 5.8 6.2 6.6 L7 5.4 L9 6 L9 8 Q9 9 8 9 Q1 8.5 1 2 Q1 1 2 1Z" fill="var(--blue)"/></svg>011521(555)0194826</p>
    </div>
  </section>

  <!-- Spanish front B -->
  <section class="card front" style="left:783px;top:109px">
    <div class="brand"><span class="brand-name">KRV</span><span class="brand-mark"></span></div>
    <div class="front-info" style="bottom:20px">
      <p class="person">Lic.Elena Varrial Soto Medina</p>
      <div class="rule"></div>
      <p class="contact">Cotizaciones en</p>
      <p class="contact">tornilleriakrv.ventas@mailbox.test</p>
      <div class="rule"></div>
      <p class="contact"><svg class="phone-icon" viewBox="0 0 10 10"><path d="M2 1 L4 1 L4.6 3 L3.4 3.8 Q4.3 5.8 6.2 6.6 L7 5.4 L9 6 L9 8 Q9 9 8 9 Q1 8.5 1 2 Q1 1 2 1Z" fill="var(--blue)"/></svg>5550172839 &nbsp;<svg class="phone-icon" viewBox="0 0 10 10"><rect x="2.5" y="0.5" width="5" height="9" rx="1" fill="none" stroke="var(--blue)" stroke-width="1.2"/></svg>5550164920</p>
    </div>
  </section>

  <!-- English back -->
  <section class="card back" style="left:95px;top:298px">
    <div class="bolt-art" role="img" aria-label="Large faint steel bolt illustration"></div>
    <div class="brand"><span class="brand-name">KRV</span><span class="brand-mark"></span></div>
    <div class="services en">
      <p>Custom Manufacturing of large Specialized Fasteners.</p>
      <p>Industrial Mining Equipment.</p>
      <p>Transportation Equipment, Trains, Ships.</p>
      <p>Farming and Construction Equipment, Tractors, Dozers</p>
      <p>Excavators, Dump Trucks.</p>
      <p>Green Energy, Wind Machines.</p>
    </div>
  </section>

  <!-- Spanish back A -->
  <section class="card back" style="left:451px;top:298px">
    <div class="bolt-art" role="img" aria-label="Large faint steel bolt illustration"></div>
    <div class="brand"><span class="brand-name">KRV</span><span class="brand-mark"></span></div>
    <div class="services es">
      <p>Fabricación especializada y Maquinados</p>
      <p>Proyectos</p><p>Mineros</p><p>Ferroviarios</p><p>Construcción</p><p>Automotrices</p>
    </div>
  </section>

  <!-- Spanish back B -->
  <section class="card back" style="left:783px;top:298px">
    <div class="bolt-art" role="img" aria-label="Large faint steel bolt illustration"></div>
    <div class="brand"><span class="brand-name">KRV</span><span class="brand-mark"></span></div>
    <div class="services es">
      <p>Fabricación especializada y Maquinados</p>
      <p>Proyectos</p><p>Mineros</p><p>Ferroviarios</p><p>Construcción</p><p>Automotrices</p>
    </div>
  </section>
</body>
</html>
```